Design a clean homepage for a travel portal based in the US catering to Asians. The design should be able to be used on other pages, or color scheme menu layout, header and footer should be usable on other pages.

Include the main options for users to click, as an example some could be; 1. Local Tour Company 2. Local Tour Guide 3. Transportation Company 4. Tour Packages

Think like www.brushmarket-example.com who brings designers and clients together we are bringing Tour company, Tour guide, Bus/Transportation company directly to those who need it. This is for a two way portal, not a common one way portal like regular booking sites.

Assume that a person arrives or is planning on arriving at a destination, what are some options that should be on the page, layout of the options: squares, rectangles, stars, scroll slides, whatever makes you feel fun, elegant, fresh, uplifting.

Feelings we want to convey: fun, elegant, fresh, uplifting, interesting, energetic

Update:
When we said this should be a simple design, we meant simple for the end user to understand what was going on. I have attached a screenshot of a website, that it is very easy to understand what its purpose is.

How you decide to set up picture/scenery areas, logo area, menu area, where the options go is all up to you. Would like it to be clean and inviting, we would also like the options to be colors that call the users to action(make them click). This doesn't have to be colors so much as design. If you have further questions feel free to message me.

Attached is our logo in various styles for you to choose from.

Target Market(s)

Travel, package tours, international students, business trips

Industry/Entity Type

Travel Industry

Number of Pages Required

1 page

Colors
ec1f27
ffffff
0255a3
474747
7f7f7f
5c5c5c
aaaaaa

Requirements
Must have
• 1. Local Tour Company 2. Local Tour Guide 3. Transportation Company 4. Tour Packages
Should not have
• Our main goal is not to sell flights or hotel rooms, so this can be an element on the page(or not) but it should not be very central/obvious.

```html
<!DOCTYPE html>
<html lang="en">
<head>
<meta charset="utf-8">
<title>Travel Portal Homepage</title>
<link rel="stylesheet" href="https://fonts.googleapis.com/css2?family=Alegreya+Sans:wght@400;500&family=Open+Sans:wght@400;700&family=Source+Sans+3:wght@400;600&display=swap">
<style>
:root{
  --red:#ec1f27;
  --white:#ffffff;
  --blue:#0255a3;
  --dark:#474747;
  --mid:#7f7f7f;
  --charcoal:#5c5c5c;
  --silver:#aaaaaa;
  --page:#efefef;
}
*{margin:0;padding:0;box-sizing:border-box}
html,body{width:1141px;height:1200px;overflow:hidden;background:var(--page)}
body{position:relative;font-family:"Source Sans 3",sans-serif;color:var(--charcoal)}
.abs{position:absolute}
.site-header{left:0;top:0;width:1141px;height:110px;background:var(--page)}
.main-nav{left:173px;top:70px;display:flex;font-family:"Alegreya Sans",sans-serif;font-size:20px;color:var(--red)}
.main-nav a{color:inherit;text-decoration:none;position:absolute;white-space:nowrap}
.nav-active-bar{left:245px;top:104px;width:78px;height:6px;background:var(--red)}
.account-links{left:880px;top:41px;width:86px;text-align:right;font-size:7.5px;color:var(--mid)}
.search-box{left:830px;top:65px;width:137px;height:22px;border:1px solid var(--red);border-radius:5px;background:var(--white)}
.search-box span{position:absolute;left:10px;top:5px;font-size:8px;color:var(--red)}
.search-box svg{position:absolute;right:6px;top:3px}
.hero{left:0;top:110px;width:1141px;height:512px;background:linear-gradient(180deg,#3e4f78 0%,#6d7a8e 30%,#4d6b9c 60%,#2d4b8a 100%)}
.hero-title{left:0;top:370px;width:1141px;text-align:center;color:var(--white);font-family:"Source Sans 3",sans-serif;font-weight:400;font-size:52px;line-height:66px;letter-spacing:-1px}
.hero-arrow{top:362px}
.option{left:174px;width:256px;height:92px;color:var(--white);text-align:center;font-family:"Open Sans",sans-serif;text-decoration:none}
.option h2{font-weight:700;font-size:22px;line-height:25px}
.option .more{position:absolute;left:0;width:100%;font-size:8.5px;font-weight:700}
.option-company{top:574px;background:var(--red)}
.option-guide{top:671px;background:var(--charcoal)}
.option-transport{top:768px;background:var(--blue)}
.option-packages{top:866px;background:var(--silver)}
.section-title{font-size:28px;font-weight:400;color:var(--charcoal);letter-spacing:-.3px}
.body-text{font-size:7.8px;line-height:10px;color:var(--mid)}
.more-link{font-size:8.5px;color:var(--dark)}
.divider{left:509px;top:819px;width:457px;height:1px;background:var(--silver)}
.side-title{font-size:17px;color:var(--charcoal)}
.side-list{list-style:none;left:844px;top:942px}
.side-list li{position:relative;padding-left:19px;height:20px;font-size:7.8px;color:var(--mid)}
.side-list li::before{content:"";position:absolute;left:0;top:3px;width:5px;height:5px;border-radius:50%;background:var(--dark)}
.site-footer{left:0;top:1093px;width:1141px;height:107px;background:var(--red)}
</style>
</head>
<body>
<header class="site-header abs">
  <nav class="main-nav abs">
    <a href="#" style="left:0">Home</a>
    <a href="#" style="left:73px">About us</a>
    <a href="#" style="left:173px">Flights</a>
    <a href="#" style="left:248px">Our Tours</a>
    <a href="#" style="left:356px">Contact us</a>
  </nav>
  <div class="nav-active-bar abs"></div>
  <div class="account-links abs">Sign in / Register</div>
  <div class="search-box abs"><span>search</span>
    <svg width="15" height="15" viewBox="0 0 15 15"><circle cx="6" cy="6" r="4.5" fill="none" stroke="#ec1f27" stroke-width="1.3"/><line x1="9.3" y1="9.3" x2="13.5" y2="13.5" stroke="#ec1f27" stroke-width="1.6"/></svg>
  </div>
</header>

<section class="hero abs" role="img" aria-label="Photo of a father and son giving a high five by a harbour with a sunlit town behind"></section>
<svg class="hero-arrow abs" style="left:29px" width="18" height="26" viewBox="0 0 18 26"><polyline points="15,2 4,13 15,24" fill="none" stroke="#fff" stroke-width="3"/></svg>
<svg class="hero-arrow abs" style="left:1075px" width="18" height="26" viewBox="0 0 18 26"><polyline points="3,2 14,13 3,24" fill="none" stroke="#fff" stroke-width="3"/></svg>
<h1 class="hero-title abs">CREATING<br>UNFORGETTABLE&nbsp; MEMORIES</h1>

<a class="option option-company abs" href="#"><h2 style="padding-top:28px">Local Tour Company</h2><span class="more" style="top:62px">more &gt;&gt;</span></a>
<a class="option option-guide abs" href="#"><h2 style="padding-top:28px">Local Tour Guide</h2><span class="more" style="top:63px">more &gt;&gt;</span></a>
<a class="option option-transport abs" href="#"><h2 style="padding-top:18px">Transportation<br>Company</h2><span class="more" style="top:67px">more &gt;&gt;</span></a>
<a class="option option-packages abs" href="#"><h2 style="padding-top:29px">Tour Packages</h2><span class="more" style="top:61px">more &gt;&gt;</span></a>

<h2 class="section-title abs" style="left:510px;top:636px">Welcome to our site!</h2>
<div class="abs" style="left:509px;top:680px;width:122px;height:122px;background:linear-gradient(180deg,#6f9fd0 0%,#2f77b8 45%,#3f6a3a 80%,#29401f 100%)" role="img" aria-label="Aerial photo of a hilltop statue overlooking a bay and city"></div>
<p class="body-text abs" style="left:644px;top:679px;width:310px">Duis autem vel eum iriure dolor in hendrerit in vulputate velit esse molestie consequat, vel illum dolore eu feugiat nulla facilisis at vero eros et accumsan et iusto odio dignissim qui blandi. Duis autem vel eum iriure dolor in hendrerit in vulputate velit esse molestie consequat, vel illum dolore eu feugiat nulla facilisis at vero eros et accumsan et iusto odio dignissim qui blandi</p>
<p class="body-text abs" style="left:644px;top:739px;width:310px">Duis autem vel eum iriure dolor in hendrerit in vulputate velit esse molestie consequat, vel illum dolore eu feugiat nulla facilisis at vero eros et accumsan et iusto odio dignissim qui blandi.</p>
<a class="more-link abs" style="left:644px;top:793px">more &gt;&gt;</a>
<div class="divider abs"></div>

<h2 class="section-title abs" style="left:510px;top:843px">Weekend Getaway</h2>
<div class="abs" style="left:510px;top:888px;width:256px;height:110px;background:linear-gradient(180deg,#4a86cc 0%,#7ba7d8 35%,#b99a6e 60%,#8a6a45 100%)" role="img" aria-label="Photo of an ancient Roman amphitheatre under a blue sky"></div>
<p class="body-text abs" style="left:510px;top:1012px;width:252px">Duis autem vel eum iriure dolor in hendrerit in vulputate velit esse molestie consequat, vel illum dolore eu feugiat nulla facilisis at vero eros et accumsan et iusto odio dignissim qui blandi. Duis autem vel eum iriure dolor in hendrerit in vulputate.</p>
<a class="more-link abs" style="left:510px;top:1065px">more &gt;&gt;</a>

<h3 class="side-title abs" style="left:844px;top:855px;font-weight:400">Lorem Ipsum</h3>
<p class="body-text abs" style="left:845px;top:882px;width:122px">Duis autem vel eum iriure dolor in hendrerit in vulputate velit esse molestie consequat, vel illum dolore eu feugiat nulla facilisis at vero eros et accumsan.</p>
<ul class="side-list abs">
  <li>Duis autem vel eum</li>
  <li>Iriure dolor in</li>
  <li>Hendrerit in vulputate</li>
  <li>Velit esse molestie</li>
  <li>Dolore eu feugiat nulla</li>
  <li>Facilisis at vero eros</li>
</ul>

<footer class="site-footer abs"></footer>
</body>
</html>
```